www.brevatin.com Sales/Order Page ReDesign

We need a new and amazing design for our sales/order page to attract more costumers and new houses for our portal.

Here is the existing page with the current design: https://www.brevatin.com/sales

We are proud owners of www.sommarhytta.no and www.brevatin.com and we want more holiday home owners to join our page so that we can rent out their holiday homes and increase the number of houses on our portal.

To get more homeowners we need a sales page that can sell our products the best way possible. Therefore we want you too blow us away with a fresh, modern, easy understandable and stylish new sales/order page.

The only restrictions we give when it comes to design is that it needs to fit the existing design of our portals, the top and footer are set. Beside that we are open for everything as long as it at once give the customers impression that this is a good, professional page were they just have to put out their houses.

When it comes to content I have added two documents who include the content to put in here and some guidelines on how to organize the page. Please be creative and add necessary graphics, symbols, background pictures and what ever necessary to make this page look professional and appealing to new costumers.

Looking forward to what suggestions we are given.

We just want to inform that we have updated our brief with a much more concrete description of what content to add on the sale page, and who to structure the content on the page. Hope this helps to make suggestions easier. Looking forward to receive some good contributions.

We would just like to make sure that everyone have understood that we are not asking for a new design suggestion to our portal in general. We are only asking for a redesign of our sales/order page you find here www.brevatin.com/sales. We have to day received some designs for our front page and the design it self was good, but that's not what we are asking for this time and don't want you to use time of something we don't need at the moment. We are looking forward too se some good suggestions.

Reason: Hello. Thanks for all the great contributions we have been given so fare. We haven't been able to respond to all design and are therefore extending the deadline so that we are able to respond to the designs we have been giver and to gov time to make final changes.

Reason: We are extending the deadline to give designers time to give new suggestion based on our latest feedback today.

Reason: Extended so we can receive last design changes.

Target Market(s)

This is a presentation page where we present our product agains new home owner who we what to choose listing there property on or site.

Industry/Entity Type

Sales

Requirements
Must have
• A modern design who calms the costumer down and help them in deciding to chose us, and for them to choose us they need to trust and believe in us. Therefore your main task is to create a page that effectively informs about our product, gets the visitors attentions and make them trust us.
Nice to have
• Examples of good competitors and good order pages we like:

http://www.cabinquest.example/info/lyp?icid=IL___O_Text___top_nav_link
https://www.nestlodge.example/rooms/new
https://www.pearvix.example/phone/compare/
http://www.guestnook.example/host
Should not have
• - Bad design :-). With bad design we mean design that looks like it's made in 2 seconds by a little child.

```html
<!DOCTYPE html>
<html lang="en">
<head>
<meta charset="utf-8">
<title>Brevatin Holiday Rental – List your property</title>
<link href="https://fonts.googleapis.com/css2?family=Open+Sans:wght@400;600;700&family=Kreon:wght@300;400&display=swap" rel="stylesheet">
<style>
:root{
  --blue:#0b93d8;
  --blue-dark:#0a7fbb;
  --footer-bar:#0982c2;
  --ink:#2b2b2b;
  --muted:#555;
  --line:#d9d9d9;
  --panel:#e6e6e6;
  --gray-btn:#8e8e93;
  --white:#fff;
}
*{box-sizing:border-box;margin:0;padding:0}
html,body{width:1200px;height:2500px;overflow:hidden;background:var(--white)}
body{position:relative;font-family:"Open Sans",Arial,sans-serif;color:var(--ink)}
.abs{position:absolute}

/* header */
.site-header{left:0;top:0;width:1200px;height:100px;border-bottom:5px solid var(--blue)}
.brand{left:97px;top:26px;display:flex;align-items:center;gap:12px}
.brand-mark{width:44px;height:44px;background:var(--blue);border-radius:4px}
.brand-name{font-size:34px;font-weight:600;color:var(--blue);letter-spacing:1px;line-height:1}
.brand-sub{font-size:11px;font-weight:600;color:var(--blue);letter-spacing:1px;margin-top:2px}
.top-nav{left:625px;top:33px;display:flex;gap:8px;font-size:12px}
.top-nav .btn{height:32px;display:flex;align-items:center;justify-content:center;gap:6px;border:1px solid #ccc;color:#444;background:#fff}
.btn.lang{width:137px}
.btn.register{width:83px}
.btn.login{width:88px;background:var(--blue);border-color:var(--blue);color:#fff}
.btn.list{width:142px;background:var(--gray-btn);border-color:var(--gray-btn);color:#fff}
.flag{width:16px;height:11px;background:#c33;border:1px solid #335}

/* hero */
.hero{left:0;top:105px;width:1200px;height:467px;border-bottom:4px solid #e3e3e3;box-shadow:0 2px 3px rgba(0,0,0,.08)}
.hero-title{left:100px;top:70px;font-size:25px;font-weight:600;color:#222}
.hero-lead{left:100px;top:106px;width:560px;font-size:14.5px;line-height:21px;color:#333}
.world-map{left:147px;top:153px;width:453px;height:217px;border-radius:40px 60px 30px 70px;background:linear-gradient(135deg,#7cc9ef,#1e8fd0)}
.hero-foot{left:0;top:390px;width:1200px;text-align:center;font-size:19px;color:#333}
.business-panel{left:695px;top:72px;width:405px;height:258px;background:var(--panel)}
.panel-title{left:30px;top:14px;width:240px;text-align:center;font-family:"Kreon",Georgia,serif;font-size:32px;font-weight:300;line-height:36px;color:#333}
.panel-label{left:58px;top:100px;font-size:13px;color:#333}
.panel-select{left:62px;top:125px;width:128px;height:30px;background:#fff;border:1px solid #ccc;font-size:12px;padding:6px 10px;display:flex;justify-content:space-between}
.panel-cta{left:25px;top:178px;width:207px;height:37px;background:var(--blue);color:#fff;font-weight:600;font-size:17px;display:flex;align-items:center;justify-content:center;border-radius:2px}
.buildings{left:278px;top:70px;width:108px;height:178px;background:linear-gradient(180deg,#b9dbef,#4d9fd0)}

/* benefits */
.benefits{left:100px;top:648px;width:1000px;display:flex}
.benefit{width:200px;text-align:center;padding:0 6px}
.benefit svg{width:28px;height:28px;display:block;margin:0 auto 14px}
.benefit h3{font-size:14px;font-weight:400;color:#222;margin-bottom:6px}
.benefit.active h3{color:var(--blue)}
.benefit p{font-size:11px;line-height:15px;color:#555}

/* contact bar */
.contact-bar{left:100px;top:833px;width:1000px;height:62px;background:var(--blue);color:#fff;display:flex;align-items:center}
.contact-bar .lead{font-size:21px;padding-left:24px;width:440px}
.contact-bar .item{display:flex;align-items:center;gap:10px;font-size:18px}
.contact-bar .phone{width:175px;padding-left:28px}
.contact-bar .divider{width:1px;height:38px;background:rgba(255,255,255,.7);margin:0 28px 0 15px}

/* services */
.services-title{left:0;top:957px;width:1200px;text-align:center;font-size:25px;color:#333}
.service{width:483px;height:128px;border:1px solid #cfcfcf;background:#fff;padding:22px 18px 0 104px}
.service .icon{position:absolute;left:18px;top:28px;width:70px;height:70px;border-radius:50%}
.service h4{font-size:17px;font-weight:400;color:#222;margin-bottom:6px}
.service p{font-size:12px;line-height:17px;color:#555;text-align:justify}
.c-left{left:100px}.c-right{left:618px}

.cta-banner{left:100px;top:1973px;width:1000px;height:77px;background:var(--gray-btn);color:#fff;font-size:24px;display:flex;align-items:center;justify-content:center}

/* footer */
.site-footer{left:0;top:2110px;width:1200px;height:340px;background:var(--blue);color:#fff}
.f-col{top:48px}
.f-col h5{font-size:19px;font-weight:400;margin-bottom:18px}
.f-col li{list-style:none;font-size:14px;line-height:21px}
.f-col .sub{margin-top:22px}
.footer-map{left:892px;top:73px;width:208px;height:134px;background:linear-gradient(135deg,#ffffff,#d8eef9);border-radius:30px 50px 20px 60px;opacity:.95}
.footer-bar{left:0;top:2450px;width:1200px;height:50px;background:var(--footer-bar);color:#fff;display:flex;align-items:center;padding:0 102px;font-size:13px}
.socials{margin-left:auto;display:flex;gap:26px}
.socials span{width:18px;height:18px;border-radius:50%;background:#fff;display:block}
.tag{position:absolute;right:12px;font-size:11px}
</style>
</head>
<body>

<header class="site-header abs">
  <div class="brand abs">
    <span class="brand-mark"></span>
    <div>
      <div class="brand-name">Brevatin</div>
      <div class="brand-sub">HOLIDAY RENTAL</div>
    </div>
  </div>
  <nav class="top-nav abs">
    <span class="btn lang">Language: <span class="flag"></span> ▾</span>
    <span class="btn register">
      <svg width="11" height="12" viewBox="0 0 11 12"><rect x="1" y="5" width="9" height="7" fill="#666"/><path d="M3 5V3a2.5 2.5 0 0 1 5 0v2" fill="none" stroke="#666" stroke-width="1.5"/></svg>Register</span>
    <span class="btn login">
      <svg width="11" height="12" viewBox="0 0 11 12"><path d="M3 5V3a2.5 2.5 0 0 1 5 0" fill="none" stroke="#fff" stroke-width="1.5"/><rect x="1" y="5" width="9" height="7" fill="#fff"/></svg>Login</span>
    <span class="btn list">List your property</span>
  </nav>
</header>

<section class="hero abs">
  <h1 class="hero-title abs">Do you own or man age more then 5 properties?</h1>
  <p class="hero-lead abs">Then we both want and are ready to help you maximize your profiton your portfolio and to help to make the administration of it more efficient.</p>
  <div class="world-map abs" role="img" aria-label="Blue world map with red location pins"></div>
  <aside class="business-panel abs">
    <h2 class="panel-title abs">Tell us about your business</h2>
    <div class="panel-label abs">Number of properties:</div>
    <div class="panel-select abs"><span>5 - 5+</span><span>▾</span></div>
    <div class="panel-cta abs">GET STARTED</div>
    <div class="buildings abs" role="img" aria-label="Illustration of blue office towers"></div>
  </aside>
  <p class="hero-foot abs">And make a profiton it. You askhow? Keep reading and we will let you know how easy and hassles it is!</p>
</section>

<section class="benefits abs">
  <div class="benefit active">
    <svg viewBox="0 0 28 28"><path d="M4 14l7 8L25 4" fill="none" stroke="#0b93d8" stroke-width="4"/></svg>
    <h3>Good exposure</h3>
    <p>List across our whole network of partners</p>
  </div>
  <div class="benefit">
    <svg viewBox="0 0 28 28"><path d="M14 3l10 4v7c0 6-5 10-10 12C9 24 4 20 4 14V7z" fill="none" stroke="#333" stroke-width="2.5"/><path d="M14 6v17" stroke="#333" stroke-width="4"/></svg>
    <h3>Secure online booking</h3>
    <p>Whether you your listings with an ML feed, your website or your favorite software partner. best for you</p>
  </div>
  <div class="benefit">
    <svg viewBox="0 0 28 28"><rect x="2" y="7" width="24" height="14" fill="none" stroke="#333" stroke-width="2.5"/><circle cx="14" cy="14" r="4" fill="none" stroke="#333" stroke-width="2"/></svg>
    <h3>Flexible payment plans</h3>
    <p>Tenants expect integrate your listings with an XML feed, your website or your favorite software partner.</p>
  </div>
  <div class="benefit">
    <svg viewBox="0 0 28 28"><path d="M6 12a8 8 0 0 1 15-3M22 16a8 8 0 0 1-15 3" fill="none" stroke="#333" stroke-width="3"/><path d="M22 3v7h-7M6 25v-7h7" fill="#333"/></svg>
    <h3>Easy to get started &amp; updated</h3>
    <p>We can integrate your listings with an XML feed, your website or your favorite software partner.</p>
  </div>
  <div class="benefit">
    <svg viewBox="0 0 28 28"><circle cx="14" cy="14" r="8" fill="none" stroke="#333" stroke-width="5" stroke-dasharray="4 2.3"/><circle cx="14" cy="14" r="3" fill="#333"/></svg>
    <h3>Dedicated account manager</h3>
    <p>You will have integrate your listings with an XML feed, your website or your favorite software partner.</p>
  </div>
</section>

<section class="contact-bar abs">
  <div class="lead">Contact us if you need help to list:</div>
  <div class="item phone">
    <svg width="16" height="18" viewBox="0 0 16 18"><path d="M4 1l3 4-2 2c1 3 3 5 5 6l2-2 3 3-2 3C7 17 1 10 1 4z" fill="#fff"/></svg>+4755018820</div>
  <span class="divider"></span>
  <div class="item">
    <svg width="18" height="16" viewBox="0 0 18 16"><path d="M1 6l8-5 8 5v9H1z" fill="none" stroke="#fff" stroke-width="2"/><path d="M1 6l8 5 8-5" fill="none" stroke="#fff" stroke-width="2"/></svg>propertymanagers@brevatin.com</div>
</section>

<h2 class="services-title abs">All our announces have the following services included:</h2>

<article class="service abs c-left" style="top:1018px"><span class="icon" role="img" aria-label="Illustration of a red and white travel mascot" style="background:linear-gradient(135deg,#e44,#9bc)"></span><h4>Access Scandinavians</h4><p>Our root sare from Norway, and we know the Scandinavian markete specially good and help youg ettenants from these very travel friendly markets</p></article>
<article class="service abs c-right" style="top:1018px"><span class="icon" role="img" aria-label="Light bulb icon in a blue ring" style="background:#fff;border:3px solid var(--blue)"></span><h4>Broad exposure</h4><p>We have been from Norway, and we know the Scandinavian markete specially good and help youg ettenants from these very travel friendly</p></article>

<article class="service abs c-left" style="top:1180px"><span class="icon" role="img" aria-label="Yellow warning sign" style="background:linear-gradient(180deg,#ffd84a,#f2b100);border-radius:8px"></span><h4>Trust &amp; Safety</h4><p>You are still from Norway, and we know the Scandinavian markete specially good and help youg ettenants from these very travel friendly markets</p></article>
<article class="service abs c-right" style="top:1180px"><span class="icon" role="img" aria-label="Stack of green bank notes" style="background:linear-gradient(135deg,#8cc968,#2e7d32);border-radius:6px"></span><h4>No Traveler fees</h4><p>Unlike many other from Norway, and we know the Scandinavian markete specially good and help youg ettenants from these very travel friendly markets</p></article>

<article class="service abs c-left" style="top:1340px"><span class="icon" role="img" aria-label="Green coin with dollar sign" style="background:radial-gradient(circle at 35% 35%,#a5d97a,#3f8f2a)"></span><h4>Payments by Brevatin</h4><p>Our root sare from Norway, and we know the Scandinavian markete specially good and help youg ettenants from these very travel friendly markets</p></article>
<article class="service abs c-right" style="top:1340px"><span class="icon" role="img" aria-label="Red book now button" style="background:radial-gradient(circle at 40% 35%,#f05050,#a50d0d)"></span><h4>Online Booking</h4><p>We simplifies the, and we know the Scandinavian markete specially good and help youg ettenants from these very travel friendly markets</p></article>

<article class="service abs c-left" style="top:1500px"><span class="icon" style="background:#fff;border:5px solid #1b8a4a"><svg width="60" height="60" viewBox="0 0 60 60"><path d="M15 30l10 11 20-22" fill="none" stroke="#1b8a4a" stroke-width="7"/></svg></span><h4>Easy - to - Use Tools</h4><p>Get access too Norway, and we know the Scandinavian markete specially good and help youg ettenants from these very travel friendly markets</p></article>
<article class="service abs c-right" style="top:1500px"><span class="icon" role="img" aria-label="Green glossy question mark button" style="background:radial-gradient(circle at 40% 35%,#c8f06a,#5aa014)"></span><h4>Unlimited inquiries</h4><p>When you are from Norway, and we know the Scandinavian markete specially good and help youg ettenants from these very travel friendly markets</p></article>

<article class="service abs c-left" style="top:1660px"><span class="icon" role="img" aria-label="Photos and camera lens" style="background:linear-gradient(135deg,#d33,#333);border-radius:6px"></span><h4>Unlimited photos</h4><p>A picture saysmore Norway, and we know the Scandinavian markete specially</p></article>
<article class="service abs c-right" style="top:1660px"><span class="icon" role="img" aria-label="Calendar page showing the 17th" style="background:linear-gradient(180deg,#6aa9df 0 22%,#eef2f6 22%);border-radius:6px"></span><h4>Online calendar</h4><p>Tenants like sare from Norway, and we know the Scandinavian markete specially good and help youg ettenants from these very travel friendly markets</p></article>

<article class="service abs c-left" style="top:1822px"><span class="icon" role="img" aria-label="Folded map with location pin" style="background:linear-gradient(135deg,#7bc67b,#f3d36b,#6aa9df);border-radius:6px"></span><h4>Map and location</h4><p>Tenants sare from Norway, and we know the Scandinavian markete specially good and help youg ettenants from these very travel friendly markets</p></article>

<div class="cta-banner abs">We can't wait to also help you with getting more bookings for the future...</div>

<footer class="site-footer abs">
  <div class="f-col abs" style="left:102px"><h5>For tenants</h5><ul><li>My page</li><li>Why Brevatin?</li><li>Help</li><li>Rental terms</li></ul></div>
  <div class="f-col abs" style="left:285px"><h5>For house owners</h5><ul><li>MyAdmin</li><li>Let us rent your house</li><li>Conditions</li></ul></div>
  <div class="f-col abs" style="left:533px"><h5>Contact us</h5><ul><li>Brevatin Holiday Rental</li><li>post@brevatin.com</li><li>+47 55 01 88 20</li><li>www.brevatin.com</li></ul>
    <h5 class="sub">Opening hours</h5><ul><li>Mon - Fri: 9.00 AM - 5.00 PM</li><li>Sat - Sun: Closed</li></ul></div>
  <div class="f-col abs" style="left:787px"><h5>Destinations</h5><ul><li>Europe</li><li>North America</li><li>South America</li><li>Africa</li><li>Asia</li><li>Australia</li></ul></div>
  <div class="footer-map abs" role="img" aria-label="White world map with a red pin over Europe"></div>
</footer>
<div class="footer-bar abs">
  <span>Brevatin.com © Copyright 2014, all rights reserved</span>
  <div class="socials"><span></span><span></span><span></span><span></span></div>
  <span class="tag">M3</span>
</div>

</body>
</html>
```